Bref créative
Qalvoren Watches - Product Catalogue
Sales and Distribution
Please use some exclusive colours, similar or contrasts in order to support all types of watches’ appear pleasing and easy for eyes.
The catalogue shouldn’t be boring, a well-balanced creativity with a flair of eye-catching theme (people MUST notice it very easy! And most important of all create something that REALLY makes attention).
Miscellaneous
A Bi-Fold Professional Product Catalogue of 6 pages includes the main cover to showcase our distribution brands and latest watch designs.
The outer-side of the main cover and the inner-side should be creatively done with our corporate identity, colour and theme (new ideas and new concepts are encouraged), and inside 4 pages will contain brand name and products.
The catalogue booklet should be handy; should be attractive and industry based as we’re planning to introduce this catalogue in series of editions either monthly or quarterly.
A professionally designed catalogue with graphics & pictures using our identity and presenting us as the professional competent company that we are. This catalogue will be left behind with various resellers, retailers and other corporate groups to keep and hopefully call us when they have orders.
1.Emotional
2. Hi-class
3. Modern
4. Exciting
5. Exclusive
Main action message: "Sales & Distribution”
Further, We want you to use the word “Brand Logo” at the place where you wanted to have the brand names. And please use stock watches at the watch pictures places/positions.
Toll Free No. 9200 48716
website www.qalvorenwatches-example.com
Looking forward to your creativity!
Logo file, ai. version
Dear Designers,
Please let me know, if you find it difficult to open the attached PDF.
Thanks,
TR
Dear designers,
Its just an idea to make something attractive to the minds. But it doesnt mean the catalogue should be designed in the sameway.
Please be creative in your efforts.

```html
<!DOCTYPE html>
<html lang="en">
<head>
<meta charset="utf-8">
<title>Veltaro – Product Catalogue</title>
<link rel="stylesheet" href="https://fonts.googleapis.com/css2?family=Cinzel:wght@400;600&display=swap">
<style>
:root{
  --band:#2b2b2d;
  --band-edge:#3a3a3c;
  --olive:#9aa63a;
  --olive-soft:#b7c15a;
  --linen:#7d8891;
  --linen-dark:#66717a;
  --label:#e6e9ea;
  --rule:#b9c0c4;
  --leather:#7a4a26;
  --leather-dark:#3c2a1e;
  --orange:#e27a1f;
  --black-strap:#1d1d1f;
  --steel:#c9ccce;
  --steel-dark:#6c7074;
}
*{box-sizing:border-box;margin:0;padding:0}
html,body{width:1200px;height:833px;overflow:hidden;background:var(--band)}
.catalogue{position:relative;width:1200px;height:833px;font-family:"Cinzel",serif;color:var(--label)}
.masthead{position:absolute;left:0;top:0;width:100%;height:120px;
  background:linear-gradient(180deg,var(--band-edge),var(--band));
  display:flex;align-items:center;justify-content:center}
.brand{display:flex;align-items:center;gap:10px;margin-top:28px}
.brand-mark{width:12px;height:12px;background:var(--olive)}
.brand-name{font-weight:600;font-size:22px;letter-spacing:3px;color:var(--olive-soft)}
.rule{position:absolute;left:0;width:100%;height:5px;background:var(--olive)}
.rule-top{top:124px}
.rule-bottom{top:764px}
.showcase{position:absolute;left:0;top:132px;width:100%;height:629px;
  background:
   repeating-linear-gradient(0deg,rgba(255,255,255,.05) 0 1px,transparent 1px 3px),
   repeating-linear-gradient(90deg,rgba(0,0,0,.05) 0 1px,transparent 1px 3px),
   radial-gradient(ellipse at center,var(--linen),var(--linen-dark));
  display:grid;grid-template-columns:repeat(5,1fr);grid-template-rows:repeat(3,1fr);
  padding:22px 60px 22px 80px}
.item{display:flex;align-items:center;gap:14px}
.watch{width:62px;height:160px;border-radius:14px;
  background:
   radial-gradient(circle at 50% 50%,var(--steel) 0 26px,var(--steel-dark) 27px 30px,transparent 31px),
   linear-gradient(90deg,transparent 9px,var(--strap) 9px 53px,transparent 53px)}
.watch.leather{--strap:var(--leather)}
.watch.dark{--strap:var(--leather-dark)}
.watch.orange{--strap:var(--orange)}
.watch.black{--strap:var(--black-strap)}
.specs{list-style:none;font-size:6.5px;letter-spacing:.5px;line-height:1}
.specs li{padding:3px 0;border-bottom:1px solid var(--rule);width:70px}
.specs li:last-child{border-bottom:none}
.footer{position:absolute;left:0;top:772px;width:100%;height:61px;
  text-align:center;font-size:7px;letter-spacing:1px;color:var(--olive-soft);padding-top:20px;line-height:1.6}
</style>
</head>
<body>
<div class="catalogue">
  <header class="masthead">
    <div class="brand"><span class="brand-mark"></span><span class="brand-name">VELTARO</span></div>
  </header>
  <div class="rule rule-top"></div>

  <main class="showcase">
    <div class="item"><div class="watch leather" role="img" aria-label="Pilot watch, grey dial, brown leather strap"></div><ul class="specs"><li>PRICE 000</li><li>COLOUR GREY</li><li>LEATHER</li><li>CODE 2141</li></ul></div>
    <div class="item"><div class="watch dark" role="img" aria-label="Pilot watch, cream dial, dark leather strap"></div><ul class="specs"><li>PRICE 000</li><li>COLOUR CREAM</li><li>LEATHER</li><li>CODE 2142</li></ul></div>
    <div class="item"><div class="watch leather" role="img" aria-label="Chronograph, silver dial, brown leather strap"></div><ul class="specs"><li>PRICE 000</li><li>COLOUR SILVER</li><li>LEATHER</li><li>CODE 2143</li></ul></div>
    <div class="item"><div class="watch black" role="img" aria-label="Chronograph, white dial, black strap"></div><ul class="specs"><li>PRICE 000</li><li>COLOUR WHITE</li><li>RUBBER</li><li>CODE 2144</li></ul></div>
    <div class="item"><div class="watch dark" role="img" aria-label="Pilot watch, black dial, dark brown strap"></div><ul class="specs"><li>PRICE 000</li><li>COLOUR BLACK</li><li>LEATHER</li><li>CODE 2145</li></ul></div>

    <div class="item"><div class="watch orange" role="img" aria-label="Sport watch, black dial, orange strap"></div><ul class="specs"><li>PRICE 000</li><li>COLOUR BLACK</li><li>LEATHER</li><li>CODE 2146</li></ul></div>
    <div class="item"><div class="watch dark" role="img" aria-label="Pilot watch, black dial, dark strap"></div><ul class="specs"><li>PRICE 000</li><li>COLOUR BLACK</li><li>LEATHER</li><li>CODE 2147</li></ul></div>
    <div class="item"><div class="watch leather" role="img" aria-label="Skeleton watch, brown leather strap"></div><ul class="specs"><li>PRICE 000</li><li>COLOUR BLACK</li><li>LEATHER</li><li>CODE 2148</li></ul></div>
    <div class="item"><div class="watch black" role="img" aria-label="Black chronograph, black strap"></div><ul class="specs"><li>PRICE 000</li><li>COLOUR BLACK</li><li>RUBBER</li><li>CODE 2149</li></ul></div>
    <div class="item"><div class="watch dark" role="img" aria-label="Chronograph, silver dial, brown strap"></div><ul class="specs"><li>PRICE 000</li><li>COLOUR SILVER</li><li>LEATHER</li><li>CODE 2150</li></ul></div>

    <div class="item"><div class="watch leather" role="img" aria-label="Chronograph, white dial, tan leather strap"></div><ul class="specs"><li>PRICE 000</li><li>COLOUR WHITE</li><li>LEATHER</li><li>CODE 2151</li></ul></div>
    <div class="item"><div class="watch black" role="img" aria-label="Black chronograph, black strap"></div><ul class="specs"><li>PRICE 000</li><li>COLOUR BLACK</li><li>RUBBER</li><li>CODE 2152</li></ul></div>
    <div class="item"><div class="watch orange" role="img" aria-label="Pilot watch, black dial, orange strap"></div><ul class="specs"><li>PRICE 000</li><li>COLOUR BLACK</li><li>LEATHER</li><li>CODE 2153</li></ul></div>
    <div class="item"><div class="watch leather" role="img" aria-label="Pilot watch, grey dial, brown strap"></div><ul class="specs"><li>PRICE 000</li><li>COLOUR GREY</li><li>LEATHER</li><li>CODE 2154</li></ul></div>
    <div class="item"><div class="watch dark" role="img" aria-label="Pilot watch, cream dial, dark strap"></div><ul class="specs"><li>PRICE 000</li><li>COLOUR CREAM</li><li>LEATHER</li><li>CODE 2155</li></ul></div>
  </main>

  <div class="rule rule-bottom"></div>
  <footer class="footer">
    <p>WWW.QALVORENWATCHES-EXAMPLE.COM</p>
    <p>SALES &amp; DISTRIBUTION TOLL FREE 9200 48716</p>
  </footer>
</div>
</body>
</html>
```